Licensed Fabrication Operator Training Program

We need a flyer to advertise a training program to business. I will attach a rough draft "original file" that we need enhanced to look professional. Details to the program are here https://www.vornelskills.org/credentials/fabrication-credential-lfo/ We want it to look clean and professional.

Please use the information that is on the "original file" rough draft. I have attached an example pdf, the reason I don't like the example is because it has too many words and looks out of date.

Font styles to use
Serif
Sans Serif

```html
<!DOCTYPE html>
<html lang="en">
<head>
<meta charset="utf-8">
<title>Licensed Fabrication Operator Program</title>
<link href="https://fonts.googleapis.com/css2?family=Bebas+Neue&family=Montserrat:wght@500;600&family=Mulish:wght@400;600;700&display=swap" rel="stylesheet">
<style>
:root{
  --blue:#0a6fc2;
  --blue-deep:#0b5ea8;
  --ink:#141414;
  --grey:#5a5a5a;
  --text:#3d3d3d;
  --white:#ffffff;
}
*{margin:0;padding:0;box-sizing:border-box}
html,body{width:1200px;height:1029px;overflow:hidden;background:var(--white)}
.flyer{position:relative;width:1200px;height:1029px;background:var(--white);font-family:"Mulish",sans-serif;color:var(--text);overflow:hidden}
.abs{position:absolute}

.tile{position:absolute;width:154px;height:130px;background:var(--blue)}
.tile .face{height:93px;background:var(--ink);color:var(--white);text-align:center;padding-top:14px;box-shadow:0 4px 6px rgba(0,0,0,.35)}
.tile .big{font-family:"Bebas Neue",sans-serif;font-size:42px;line-height:38px}
.tile .small{font-family:"Montserrat",sans-serif;font-weight:500;font-size:15px;line-height:20px;white-space:nowrap}

.title-top{left:584px;top:44px;font-family:"Montserrat",sans-serif;font-weight:600;font-size:84px;color:var(--grey);line-height:96px;letter-spacing:1px;white-space:nowrap}
.title-main{left:580px;top:140px;font-family:"Bebas Neue",sans-serif;font-size:150px;line-height:140px;color:var(--blue);white-space:nowrap}
.title-sub{left:584px;top:280px;font-family:"Montserrat",sans-serif;font-weight:600;font-size:48px;line-height:52px;color:var(--grey);white-space:nowrap}
.seal{left:1048px;top:46px}

.pill{left:40px;top:367px;width:184px;height:36px;border-radius:18px;background:var(--blue);color:var(--white);font-family:"Montserrat",sans-serif;font-weight:600;font-size:19px;line-height:36px;text-align:center}
.skills{list-style:none;font-size:16px;color:var(--text)}
.skills li{height:30.5px;display:flex;align-items:center;gap:10px;white-space:nowrap}
.skills svg{flex:none}

.quote-bar{left:0;top:613px;width:15px;height:207px;background:var(--blue)}
.quote{left:39px;top:620px;width:406px;font-size:16px;line-height:24px;text-align:justify}
.members{left:39px;top:791px;font-size:16px;white-space:nowrap}

.partner{position:absolute;display:flex;align-items:center;gap:6px;font-family:"Mulish",sans-serif;font-weight:700;font-size:19px;color:var(--ink);white-space:nowrap}
.partner .dot{width:12px;height:12px;border-radius:50%;background:var(--ink)}
.seal-plain{position:absolute;left:312px;top:826px;width:54px;height:54px;background:#1f7a3a}

.equipment{left:416px;top:858px;width:304px;height:124px;background:linear-gradient(90deg,#c9ced3,#aab2ba 45%,#2c6fc0 70%,#1b56a6);border-radius:4px}

.photo{left:640px;top:365px;width:580px;height:580px;border-radius:50%;background:radial-gradient(circle at 65% 45%,#d8b49a,#b78e72 35%,#cfd6cf 70%,#9fb9a8)}
.ribbon{position:absolute;height:37px;background:var(--blue-deep);border:2px solid var(--white);color:var(--white);font-family:"Montserrat",sans-serif;font-weight:600;font-size:22px;line-height:33px;text-align:center;white-space:nowrap}

.cta{left:962px;top:832px;width:208px;text-align:center;color:var(--white)}
.cta h2{font-family:"Bebas Neue",sans-serif;font-weight:400;font-size:36px;line-height:36px;border-bottom:2px solid var(--white);display:inline-block;padding:0 2px 2px}
.cta .icons{display:flex;justify-content:center;gap:12px;margin:10px 0 6px}
.cta p{font-size:16px;line-height:29px;font-weight:600;white-space:nowrap}
</style>
</head>
<body>
<div class="flyer">

  <div class="tile" style="left:40px;top:45px"><div class="face"><div class="big">Advanced</div><div class="small">MANUFACTURING</div></div></div>
  <div class="tile" style="left:207px;top:45px"><div class="face"><div class="big">Hands-On</div><div class="small">LEARNING</div></div></div>
  <div class="tile" style="left:373px;top:45px"><div class="face"><div class="big">College</div><div class="small">CREDITS ELIGIBLE</div></div></div>
  <div class="tile" style="left:40px;top:198px"><div class="face"><div class="big">120</div><div class="small">HOURS</div></div></div>
  <div class="tile" style="left:207px;top:198px"><div class="face"><div class="big">$2500</div><div class="small">PER STUDENT</div></div></div>
  <div class="tile" style="left:373px;top:198px"><div class="face"><div class="big">STB</div><div class="small">REIMBURSEMENT</div></div></div>

  <div class="abs title-top">LICENSED</div>
  <svg class="abs seal" width="112" height="92" viewBox="0 0 112 92" role="img" aria-label="Program seal">
    <circle cx="56" cy="46" r="42" fill="#c9cdd3"/>
    <circle cx="56" cy="46" r="32" fill="#1f3f86"/>
  </svg>
  <div class="abs title-main">FABRICATION</div>
  <div class="abs title-sub">OPERATOR PROGRAM</div>

  <div class="abs pill">SKILLS TAUGHT</div>
  <ul class="abs skills" style="left:40px;top:413px">
    <li><svg width="16" height="16" viewBox="0 0 16 16"><circle cx="8" cy="8" r="6.5" fill="none" stroke="#0a6fc2" stroke-width="1.6"/><path d="M5 8l2.2 2.2L12 5" fill="none" stroke="#0a6fc2" stroke-width="1.8"/></svg>Communication.</li>
    <li><svg width="16" height="16" viewBox="0 0 16 16"><circle cx="8" cy="8" r="6.5" fill="none" stroke="#0a6fc2" stroke-width="1.6"/><path d="M5 8l2.2 2.2L12 5" fill="none" stroke="#0a6fc2" stroke-width="1.8"/></svg>Lean Principles.</li>
    <li><svg width="16" height="16" viewBox="0 0 16 16"><circle cx="8" cy="8" r="6.5" fill="none" stroke="#0a6fc2" stroke-width="1.6"/><path d="M5 8l2.2 2.2L12 5" fill="none" stroke="#0a6fc2" stroke-width="1.8"/></svg>Problem Solving.</li>
    <li><svg width="16" height="16" viewBox="0 0 16 16"><circle cx="8" cy="8" r="6.5" fill="none" stroke="#0a6fc2" stroke-width="1.6"/><path d="M5 8l2.2 2.2L12 5" fill="none" stroke="#0a6fc2" stroke-width="1.8"/></svg>Teamwork.</li>
    <li><svg width="16" height="16" viewBox="0 0 16 16"><circle cx="8" cy="8" r="6.5" fill="none" stroke="#0a6fc2" stroke-width="1.6"/><path d="M5 8l2.2 2.2L12 5" fill="none" stroke="#0a6fc2" stroke-width="1.8"/></svg>Locating Information.</li>
    <li><svg width="16" height="16" viewBox="0 0 16 16"><circle cx="8" cy="8" r="6.5" fill="none" stroke="#0a6fc2" stroke-width="1.6"/><path d="M5 8l2.2 2.2L12 5" fill="none" stroke="#0a6fc2" stroke-width="1.8"/></svg>Supply Chain &amp; Logistics.</li>
  </ul>
  <ul class="abs skills" style="left:279px;top:413px">
    <li><svg width="16" height="16" viewBox="0 0 16 16"><circle cx="8" cy="8" r="6.5" fill="none" stroke="#0a6fc2" stroke-width="1.6"/><path d="M5 8l2.2 2.2L12 5" fill="none" stroke="#0a6fc2" stroke-width="1.8"/></svg>Data Analysis.</li>
    <li><svg width="16" height="16" viewBox="0 0 16 16"><circle cx="8" cy="8" r="6.5" fill="none" stroke="#0a6fc2" stroke-width="1.6"/><path d="M5 8l2.2 2.2L12 5" fill="none" stroke="#0a6fc2" stroke-width="1.8"/></svg>Total Productive Maintenance.</li>
    <li><svg width="16" height="16" viewBox="0 0 16 16"><circle cx="8" cy="8" r="6.5" fill="none" stroke="#0a6fc2" stroke-width="1.6"/><path d="M5 8l2.2 2.2L12 5" fill="none" stroke="#0a6fc2" stroke-width="1.8"/></svg>Autonomous Maintenance.</li>
    <li><svg width="16" height="16" viewBox="0 0 16 16"><circle cx="8" cy="8" r="6.5" fill="none" stroke="#0a6fc2" stroke-width="1.6"/><path d="M5 8l2.2 2.2L12 5" fill="none" stroke="#0a6fc2" stroke-width="1.8"/></svg>Customer Service.</li>
    <li><svg width="16" height="16" viewBox="0 0 16 16"><circle cx="8" cy="8" r="6.5" fill="none" stroke="#0a6fc2" stroke-width="1.6"/><path d="M5 8l2.2 2.2L12 5" fill="none" stroke="#0a6fc2" stroke-width="1.8"/></svg>Project Management.</li>
  </ul>

  <div class="abs quote-bar"></div>
  <p class="abs quote">We feel that Vornel LFO certification compliments not only the qualifications of the candidates we see, but also enhances the knowledge, skills, &amp; abilities of existing team members in our pursuit of manufacturing excellence. “ - Dale Marrick Vice President &amp; General Manager Corvane Manufacturing.</p>
  <p class="abs members">Vornel certification Scheme Committee Members Work at</p>

  <div class="partner" style="left:40px;top:878px"><span class="dot"></span>HALDEN</div>
  <div class="partner" style="left:150px;top:878px"><span class="dot"></span>NORSTAND</div>
  <div class="seal-plain" role="img" aria-label="Accreditation badge"></div>
  <div class="partner" style="left:309px;top:886px;font-size:14px">VERITAB</div>
  <div class="partner" style="left:40px;top:950px"><span class="dot"></span>KELTON</div>
  <div class="partner" style="left:170px;top:950px"><span class="dot"></span>ARVEX</div>
  <div class="partner" style="left:290px;top:950px"><span class="dot"></span>VORNEL</div>

  <div class="abs equipment" role="img" aria-label="Training equipment: pneumatic trainer bench and blue control cabinet"></div>

  <div class="abs photo" role="img" aria-label="Photo of smiling trainees in a classroom"></div>
  <svg class="abs" style="left:0;top:0" width="1200" height="1029" viewBox="0 0 1200 1029">
    <path d="M676 824 A 305 305 0 1 1 1200 513" fill="none" stroke="#0a6fc2" stroke-width="14"/>
    <path d="M653 1029 C 900 960 1120 800 1200 380 L1200 1029 Z" fill="#0a6fc2"/>
    <path d="M700 1000 C 930 930 1140 760 1200 440" fill="none" stroke="#1b80d0" stroke-width="3" opacity=".6"/>
  </svg>

  <div class="ribbon" style="left:561px;top:550px;width:184px">SAFETY</div>
  <div class="ribbon" style="left:538px;top:611px;width:230px">QUALITY</div>
  <div class="ribbon" style="left:522px;top:671px;width:262px">PROCESSES</div>
  <div class="ribbon" style="left:476px;top:732px;width:357px">MAINTENANCE AWARENESS</div>

  <div class="abs cta">
    <h2>CALL TO SCHEDULE</h2>
    <div class="icons">
      <svg width="18" height="18" viewBox="0 0 18 18"><circle cx="9" cy="9" r="9" fill="#fff"/><path d="M6 5l2 2-1 1.2c.6 1.2 1.6 2.2 2.8 2.8L11 10l2 2-1.3 1.3C8.7 13 5 9.3 4.7 6.3z" fill="#0a6fc2"/></svg>
      <svg width="18" height="18" viewBox="0 0 18 18"><circle cx="9" cy="9" r="9" fill="#fff"/><rect x="4.5" y="6" width="9" height="6.5" fill="#0a6fc2"/><path d="M4.5 6l4.5 3.5L13.5 6" fill="none" stroke="#fff" stroke-width="1"/></svg>
    </div>
    <p>209 555 0146<br>dale@northlinelean.com<br>On - site training available</p>
  </div>

</div>
</body>
</html>
```